THE REVEL OF GLIMBROOK Prospectus/Deck

We need a prospectus/deck made for this Halloween event called THE REVEL OF GLIMBROOK. Attached is the writeup, our logo, some background photos you can use, and photos of the actual town site. For the town photos (4) could you try to make them look greyscale or smokey? I attached a sample Prospectus/Deck that was created for another event of ours to give you an idea of layout and pages.

```html
<!DOCTYPE html>
<html lang="en">
<head>
<meta charset="utf-8">
<title>The Revel of Glimbrook – Prospectus</title>
<link rel="stylesheet" href="https://fonts.googleapis.com/css2?family=Amatic+SC:wght@700&family=Roboto+Condensed:wght@400&display=swap">
<style>
  :root{
    --board:#dcdcde;
    --ink-black:#080808;
    --slime:#86a843;
    --slime-bright:#93b64a;
    --panel-dark:rgba(22,24,28,.9);
    --panel-green:#2b4440;
    --teal-deep:#0f3a36;
    --teal-mid:#2f7c74;
    --white:#ffffff;
    --body-light:#e8ece8;
    --display:"Amatic SC", "Arial Narrow", sans-serif;
    --text:"Roboto Condensed", "Arial Narrow", sans-serif;
  }
  *{box-sizing:border-box;margin:0;padding:0}
  html,body{width:1200px;height:1069px;overflow:hidden;background:var(--board)}
  .board{position:relative;width:1200px;height:1069px}
  .slide{position:absolute;width:498px;height:280px;overflow:hidden;box-shadow:1px 2px 4px rgba(0,0,0,.35)}
  .slide--cover{left:364px;top:83px;background:var(--ink-black)}
  .slide--intro{left:107px;top:404px}
  .slide--vendors{left:647px;top:404px}
  .slide--about{left:107px;top:706px}
  .slide--food{left:647px;top:706px}

  .photo{position:absolute}
  .heading{position:absolute;font-family:var(--display);font-weight:700;color:var(--slime);line-height:1;text-transform:uppercase}
  .body{position:absolute;font-family:var(--text);color:var(--body-light)}

  /* cover */
  .cover-name{position:absolute;left:0;right:0;top:36px;text-align:center;font-family:var(--display);font-weight:700;font-size:50px;line-height:1;color:var(--slime-bright);letter-spacing:1px}
  .cover-photo{left:0;top:132px;width:478px;height:148px;background:linear-gradient(170deg,#8c9088 0%,#4d554b 30%,#2b3028 60%,#12140f 100%)}

  /* intro */
  .intro-photo{inset:0;background:radial-gradient(ellipse at 70% 45%,#3f8c99 0%,#1f5a6e 35%,#15304e 70%,#0c1530 100%)}
  .intro-panel{position:absolute;left:11px;top:0;width:217px;height:250px;background:var(--panel-dark);clip-path:polygon(0 0,100% 0,100% 85%,0 100%)}
  .intro-wedge{position:absolute;inset:0;background:var(--slime);clip-path:polygon(100% 82.5%,100% 100%,65% 100%)}
  .intro-title{left:28px;top:19px;font-size:32px}
  .intro-welcome{position:absolute;left:28px;top:64px;font-family:var(--display);font-weight:700;font-size:11px;color:var(--white);text-transform:uppercase}
  .intro-copy{left:28px;top:84px;width:172px;font-size:5.1px;line-height:7.4px}
  .intro-copy p+p{margin-top:7px}

  /* vendors */
  .vendors-texture{inset:0;background:radial-gradient(ellipse at 50% 60%,#d9d9d9 0%,#a9a9a9 55%,#6e6e6e 100%)}
  .vendors-panel{position:absolute;left:0;top:6px;width:487px;height:204px;background:var(--panel-green)}
  .vendors-title{left:26px;top:13px;font-size:32px}
  .vendors-rate{position:absolute;left:26px;top:56px;width:330px;font-family:var(--display);font-weight:700;font-size:13px;line-height:15px;color:var(--slime);text-transform:uppercase}
  .vendors-copy{left:26px;top:118px;width:170px;font-size:6.8px;line-height:9.4px}
  .vendors-list{left:249px;top:118px;font-size:6.8px;line-height:9.4px;list-style:none}

  /* about */
  .about-photo{inset:0;background:linear-gradient(160deg,#3c433a 0%,#2b302b 45%,#1c1f1c 100%)}
  .about-title{left:28px;top:13px;font-size:30px}
  .about-copy{left:28px;top:67px;width:318px;font-size:8.3px;line-height:10.7px}
  .about-details{position:absolute;left:28px;top:144px;font-family:var(--display);font-weight:700;font-size:14px;line-height:20.5px;color:var(--slime);text-transform:uppercase;list-style:none}

  /* food */
  .food-photo{inset:0;background:radial-gradient(ellipse at 55% 70%,var(--teal-mid) 0%,#1f5a54 45%,var(--teal-deep) 80%,#0a2724 100%)}
  .food-title{left:24px;top:8px;font-size:38px;line-height:37px;color:var(--white)}
  .food-copy{left:24px;top:89px;width:345px;font-size:6.9px;line-height:9.4px}
  .food-copy p+p{margin-top:9px}
</style>
</head>
<body>
<main class="board">

  <section class="slide slide--cover">
    <div class="cover-name">THE REVEL OF GLIMBROOK</div>
    <div class="photo cover-photo" role="img" aria-label="Smoky greyscale aerial photo of the town site at dusk"></div>
  </section>

  <section class="slide slide--intro">
    <div class="photo intro-photo" role="img" aria-label="Foggy blue forest scene with a hooded scythe-bearer among trees"></div>
    <div class="intro-wedge"></div>
    <div class="intro-panel"></div>
    <h2 class="heading intro-title">Introduction:</h2>
    <p class="intro-welcome">Welcome to The Revel of Glimbrook,</p>
    <div class="body intro-copy">
      <p>where terror meets Hollywood magic! Step into our nightmare-inducing event set within a sprawling film studio lot at 1450 Concession 9, Ashgrove, Ontario L0B 2K0 which has been transformed into a chillingly realistic little town. As you enter, you will find yourself immersed in the eerie atmosphere of a bygone era, where each corner holds lurking horrors. Our haunted experience offers a unique opportunity for vendors to become part of the terror by occupying the shops that line the Main Street of this sinister town. From creepy curiosities to spine-chilling treats, your store front will become a focal point of fear, allowing visitors to not only scream but also shop amidst the horrors. Prepare for a spine-tingling journey like no other as you explore our haunted event in this hauntingly realistic town.</p>
      <p>The Revel of Glimbrook is an an exhilarating and spine-chilling haunted town experience that promises to deliver unforgettable thrills and scares. As we gear up for another terrifying season, we invite you to join us as a valued vendor or sponsor. This prospectus outlines the various opportunities available for your brand to be part of this highly anticipated event.</p>
    </div>
  </section>

  <section class="slide slide--vendors">
    <div class="photo vendors-texture" role="img" aria-label="Grey grunge texture with cracks and splatter"></div>
    <div class="vendors-panel"></div>
    <h2 class="heading vendors-title">Vendor Opportunities:</h2>
    <p class="vendors-rate">On-site vendors: starting at $2500 + HST (per vendor; no sharing) depending on location and type of products/services sold and offered.</p>
    <p class="body vendors-copy">Set up your booth within the haunted town premises and showcase your products or services to a captive audience in one of the existing buildings. Your brand will be exposed to thousands of visitors throughout the event. Examples of suitable vendors include:</p>
    <ul class="body vendors-list">
      <li>Halloween costume shops</li>
      <li>Horror-themed merchandise</li>
      <li>Local/Artisan food vendors (pre-packaged items)</li>
      <li>Face painting and special effects makeup artists</li>
      <li>Paranormal investigators or ghost tour guides</li>
      <li>Novelty and souvenir vendors</li>
      <li>Psychic</li>
      <li>Metaphysical items and crystals</li>
    </ul>
  </section>

  <section class="slide slide--about">
    <div class="photo about-photo" role="img" aria-label="Darkened aerial photo of the town streets and rooftops"></div>
    <h2 class="heading about-title">About The Revel of Glimbrook</h2>
    <p class="body about-copy">The Revel of Glimbrook is a premier haunted town attraction known for its immersive and interactive experience that pushes the boundaries of fear. Our haunted town offers a meticulously designed setting with elaborate sets, talented actors, and cutting-edge special effects to create an atmosphere of horror and suspense. We attract a diverse audience of thrill-seekers, horror enthusiasts, families, and groups of friends, ensuring a wide reach for your brand.</p>
    <ul class="about-details">
      <li>Event Details: Date: October 6 – 31, 2023 (17 days)</li>
      <li>Location: 1450 Concession 9, Ashgrove, Ontario L0B 2K0</li>
      <li>Website: www.revelofglimbrook.ca</li>
    </ul>
  </section>

  <section class="slide slide--food">
    <div class="photo food-photo" role="img" aria-label="Teal night scene with a bare twisted tree silhouette and a bat"></div>
    <h2 class="heading food-title">Food Trucks $5000 + HST<br>Max of 3-4 total</h2>
    <div class="body food-copy">
      <p>Promotional Giveaways: Partner with us to provide branded merchandise or samples to be distributed to our visitors. This opportunity allows you to directly engage with attendees and create lasting impressions of your brand.</p>
      <p>Exclusive Sponsorship: Become an exclusive sponsor of The Revel of Glimbrook. This comprehensive package offers maximum exposure and recognition for your brand. Benefits may include prominent logo placement, branding on event merchandise, on-site signage, social media promotions, and more. This option is ideal for businesses looking to establish a strong association with the haunted town and its audience.</p>
    </div>
  </section>

</main>
</body>
</html>
```